Website for Brisbeck Current Glide

Require a website for a river float in the City of Kellsford. Located on Brisbeck River River. Will need to be a coded website with incorporated booking system through Fare Harbor software.

Pages include
Home
Pricing
About
FAQ
Contact

Brisbeck Current Glide is an activity based business that will have customers floating down the Brisbeck River river in Kellsford AB. The site will have all information needed and a full reservation system. The project was launched to provide people in the Kellsford area a favorite summer activity.

Here are similar websites to reference what our business will be doing and what we are looking for.

mellowbendcanoehire.example
pinegulchloopers.example

Target Market(s)

Families, Groups, Individuals, Anyone who wants to explore the river

Industry/Entity Type

Activities based business/ Outdoor recreational/ River Float

Coding

Coded - Design and coding required

Number of Pages Required

5+ page

Colors
0054AA
0677BA
7BADD7
CADEEF
E8F1F8
F0912C
F2A743
F7CA91
FBE8D2
FDF5EE

```html
<!DOCTYPE html>
<html lang="en">
<head>
<meta charset="utf-8">
<title>Brisbeck Current Glide</title>
<link href="https://fonts.googleapis.com/css2?family=Poppins:wght@400;500;600;700&display=swap" rel="stylesheet">
<style>
:root{
  --navy:#0c2d66;
  --navy-deep:#0a2a5e;
  --sky:#58c6e8;
  --sky-shadow:#274a6e;
  --ink:#111;
  --white:#fff;
  --rule:#d6d6d6;
  --footer-rule:#3b5687;
}
*{margin:0;padding:0;box-sizing:border-box}
html,body{width:1200px;height:2640px;overflow:hidden;background:var(--white)}
body{position:relative;font-family:"Poppins",sans-serif;color:var(--navy)}
.abs{position:absolute}

.brand{left:0;width:1200px;top:58px;display:flex;justify-content:center;align-items:center;gap:14px}
.brand-dot{width:46px;height:46px;border-radius:50%;background:var(--sky)}
.brand-name{font-size:34px;font-weight:700;color:var(--navy);letter-spacing:.5px}

.header-rule{left:86px;width:1028px;top:188px;height:1px;background:var(--rule)}
.main-nav{left:0;width:1200px;top:200px;display:flex;justify-content:center;gap:28px;font-size:15px;font-weight:500;color:var(--ink)}
.main-nav .current{color:var(--sky)}

.hero{left:86px;top:240px;width:1028px;height:456px;
  background:linear-gradient(180deg,#f1e6d2 0%,#cfc6b4 35%,#7f9a6d 58%,#6e9aa0 75%,#5e8a45 100%)}
.hero-title{left:86px;width:1028px;top:395px;text-align:center;font-size:66px;font-weight:700;color:var(--white);
  letter-spacing:-1px;text-shadow:3px 3px 4px rgba(0,0,0,.55)}
.hero-sub{left:344px;width:511px;top:482px;height:21px;background:var(--white);text-align:center;font-size:15px;line-height:21px;color:var(--ink)}

.btn{display:flex;align-items:center;justify-content:center;background:var(--sky);color:var(--white);
  border-radius:30px;font-size:21px;font-weight:500;box-shadow:5px 5px 0 var(--sky-shadow)}
.hero-btn{left:513px;top:520px;width:172px;height:58px}

.shuttle-photo{left:0;top:824px;width:599px;height:452px;
  background:linear-gradient(180deg,#3f6b2c 0%,#6e9a3e 35%,#a88fb9 48%,#7fa968 62%,#9fb99a 100%)}
.shuttle-title{left:654px;top:890px;width:440px;font-size:39px;font-weight:600;line-height:45px;color:var(--navy)}
.shuttle-text{left:655px;top:1003px;width:475px;font-size:16px;line-height:25px;color:var(--navy)}
.shuttle-btn{left:655px;top:1103px;width:171px;height:58px}

.week-title{left:0;width:1200px;top:1392px;text-align:center;font-size:39px;font-weight:600;color:var(--navy)}
.week-photo{left:86px;top:1477px;width:1028px;height:414px;
  background:linear-gradient(180deg,#c9cfb8 0%,#8fa56a 30%,#d08a4e 52%,#c9d2d4 72%,#eef1f1 100%)}
.week-text{left:120px;width:960px;top:1922px;text-align:center;font-size:16px;line-height:25px;color:var(--navy)}
.week-btn{left:509px;top:2017px;width:172px;height:58px}

.site-footer{left:0;top:2210px;width:1200px;height:430px;background:var(--navy-deep);color:var(--white)}
.foot-col{position:absolute;text-align:center}
.foot-head{font-size:20px;font-weight:600}
.foot-bar{width:28px;height:2px;background:var(--white);margin:10px auto 0}
.connect{left:48px;width:400px;top:76px;font-size:16px;line-height:27px}
.connect b{font-weight:600}
.socials{display:flex;justify-content:center;gap:12px;margin-top:20px}
.social-box{width:42px;height:42px;border-radius:6px;background:#2d4b80;display:flex;align-items:center;justify-content:center}
.social-box span{width:12px;height:12px;border-radius:50%;border:2px solid var(--white)}
.signup{margin-top:18px}
.signup a{color:var(--sky);font-weight:600;text-decoration:none}
.footer-brand{left:400px;width:400px;top:200px}
.footer-brand .name{display:flex;justify-content:center;align-items:center;gap:10px;font-size:24px;font-weight:700}
.footer-brand .dot{width:34px;height:34px;border-radius:50%;background:var(--sky)}
.footer-brand .tag{font-size:16px;margin-top:16px}
.foot-nav{left:751px;width:400px;top:76px}
.foot-nav ul{list-style:none;margin-top:18px;font-size:16px}
.foot-nav li{height:39px;line-height:39px}
.footer-rule{left:86px;width:1028px;top:2575px;height:1px;background:var(--footer-rule)}
.copyright{left:0;width:1200px;top:2589px;text-align:center;font-size:16px;color:var(--white)}
</style>
</head>
<body>
  <div class="abs brand"><span class="brand-dot"></span><span class="brand-name">Brisbeck Current Glide</span></div>
  <div class="abs header-rule"></div>
  <nav class="abs main-nav"><span class="current">HOME</span><span>PRICING</span><span>ABOUT</span><span>FAQ</span><span>CONTACT</span></nav>

  <div class="abs hero" role="img" aria-label="City skyline above the river with a bridge and green riverbank"></div>
  <h1 class="abs hero-title">BRISBECK CURRENT GLIDE</h1>
  <div class="abs hero-sub">Float the Brisbeck River through downtown Kellsford</div>
  <a class="abs btn hero-btn">Book Now</a>

  <div class="abs shuttle-photo" role="img" aria-label="Float tube drifting down a tree-lined river with wildflowers"></div>
  <h2 class="abs shuttle-title">Shuttle Service And Gear Included</h2>
  <p class="abs shuttle-text">We provide everything you need including round trip shuttle service, float tube, lifejacket, paddle, and more. Fun for everyone!</p>
  <a class="abs btn shuttle-btn">Learn More</a>

  <h2 class="abs week-title">Floating 7 &amp; Days A Week</h2>
  <div class="abs week-photo" role="img" aria-label="Friends paddling kayaks on a calm river"></div>
  <p class="abs week-text">Our priority is to make sure everyone has a safe and fun time on the river. Safety demonstrations are provided and staff are available to assist in any way. Whether you are a family with children, larger group or just want a relaxing way to explore the river, this is a must try activity.</p>
  <a class="abs btn week-btn">Book Now</a>

  <footer class="abs site-footer">
    <div class="foot-col connect">
      <div class="foot-head">Connect</div>
      <div class="foot-bar"></div>
      <div style="margin-top:20px"><b>EMAIL:</b> info@brisbeckglide.example</div>
      <div><b>LOCATION:</b> Willowbank Landing</div>
      <div class="socials">
        <span class="social-box" aria-label="Social link"><span></span></span>
        <span class="social-box" aria-label="Social link"><span></span></span>
        <span class="social-box" aria-label="Review link"><span></span></span>
      </div>
      <div class="signup"><a>Sign up</a> for our mailing list</div>
    </div>
    <div class="foot-col footer-brand">
      <div class="name"><span class="dot"></span>Brisbeck Current Glide</div>
      <div class="tag">Floating 7 days a week</div>
    </div>
    <div class="foot-col foot-nav">
      <div class="foot-head">Main Navigation</div>
      <div class="foot-bar"></div>
      <ul><li>Home</li><li>Pricing</li><li>About</li><li>FAQ</li><li>Contact</li></ul>
    </div>
  </footer>
  <div class="abs footer-rule"></div>
  <div class="abs copyright">Copyright 2022.Brisbeck Current Glide.All right reserved.</div>
</body>
</html>
```